Design refresh required for educational resources

A full redesign/refresh is required for an education resource kit.
The final outputs will include:
- Powerpoint slide template
- parent handout template
- overview template
- 2 different types of lesson plan templates (can be related but need to have some differences to distinguish between the two)
- 2 x branded labels for resources
- teacher 'intervention plan' summary sheet
- 'scope and sequence' document
Design needs to have a fun, modern feel, capturing elements of the New Zealand landscape, flora and/or fauna.
The resources will be used as part of a teaching kit for use in schools.
Please see attached files for existing samples of some of the above documents. Full content to be provided for successful applicant.
Please submit sample of one or two of the documents to bid for this work - enough so that I can see the overall design aesthetic you are proposing.
New Zealand teachers and parents of 5 year old children

```html
<!DOCTYPE html>
<html lang="en">
<head>
<meta charset="utf-8">
<title>Bright Path Reading Approach – Family &amp; Lesson Sheets</title>
<link href="https://fonts.googleapis.com/css2?family=Lexend:wght@400;500;600&family=Lato:ital,wght@0,400;0,700;1,400&display=swap" rel="stylesheet">
<style>
:root{
  --page:#f2efed;
  --panel:#ffffff;
  --green:#64a23a;
  --green-soft:#6fa845;
  --ink:#1f1f1f;
  --body:#3a3a3a;
  --muted:#555555;
  --link:#5c9a30;
  --white:#ffffff;
}
*{box-sizing:border-box;margin:0;padding:0}
html,body{width:1200px;height:4835px;overflow:hidden;background:var(--page)}
body{position:relative;font-family:"Lato",sans-serif;color:var(--body)}
.panel{position:absolute;left:45px;width:1110px;background:var(--panel)}

/* cover */
.cover{top:71px;height:737px;overflow:hidden}
.cover-scene{position:absolute;inset:0;background:linear-gradient(180deg,#0d2a86 0%,#1f4fb0 28%,#5f8fcf 45%,#9fb6c8 52%,#3d5e49 60%,#6f8fb6 66%,#9bbbe0 80%,#6f9bd0 100%)}
.brand{position:absolute;left:0;right:0;top:300px;text-align:center;color:var(--white);font-family:"Lexend",sans-serif;font-weight:500}
.brand-mark{display:block;width:60px;height:60px;margin:0 auto 26px;border-radius:50%;background:var(--green)}
.brand-name{font-size:33px;letter-spacing:2px;line-height:40px;text-transform:uppercase}
.brand-sub{font-size:24px;line-height:34px}

/* this week */
.this-week{top:856px;height:736px;background:var(--green);color:var(--white);text-align:center;font-family:"Lexend",sans-serif}
.this-week h2{font-size:30px;font-weight:500;margin-bottom:16px}
.this-week p{font-size:17px;font-weight:400;line-height:37px}
.tw-block{position:absolute;left:0;right:0}

/* play at home */
.play{top:1643px;height:746px}
.play-photo{position:absolute;left:64px;top:115px;width:460px;height:509px;background:linear-gradient(135deg,#3d4a7a 0%,#eceae6 35%,#f1efea 55%,#e08a3a 75%,#5d3c2a 100%)}
.play-text{position:absolute;left:584px;top:110px;width:470px}
.play-text h2{font-family:"Lexend",sans-serif;font-size:36px;line-height:44px;font-weight:500;color:var(--ink);margin-bottom:24px}
.play-text p{font-size:12.5px;line-height:20px;text-align:justify;margin-bottom:16px;color:var(--body)}
.play-text .link{color:var(--link);text-decoration:underline;font-weight:700}

/* framed boxes */
.frame{position:absolute;left:64px;width:980px;border:2px solid var(--green);background:var(--panel)}
.tab{position:absolute;left:-2px;top:-2px;background:var(--green);color:var(--white);font-family:"Lexend",sans-serif;font-weight:600;display:flex;align-items:center;justify-content:center}

.lesson{top:2438px;height:736px}
.week{top:75px;height:191px}
.week .tab{width:195px;height:52px;font-size:21px}
.week-left{position:absolute;left:30px;top:74px;font-size:13.5px;line-height:22px;font-weight:700;color:var(--ink)}
.week-right{position:absolute;left:380px;top:28px;font-size:14px;line-height:26px;color:var(--body)}
.section-head{position:absolute;left:0;right:0;text-align:center}
.section-head h2{font-family:"Lexend",sans-serif;font-weight:500;font-size:26px;color:var(--ink);margin-bottom:14px}
.section-head p{font-size:16.5px;color:var(--body)}
.day .tab{width:113px;height:83px;font-size:19px}
.day-lead{position:absolute;left:160px;font-size:16.5px;line-height:27px;font-weight:700;color:var(--ink)}
.day-body{position:absolute;left:32px;right:32px;font-size:16.5px;line-height:27px;color:var(--body)}
.day-body b{color:var(--ink)}

.pa{top:3223px;height:743px}

/* segmenting */
.seg{top:4011px;height:746px;text-align:center}
.seg h2{position:absolute;left:0;right:0;top:136px;font-family:"Lexend",sans-serif;font-weight:500;font-size:39px;color:var(--ink)}
.seg-sub{position:absolute;left:0;right:0;top:196px;font-size:12.5px}
.seg-body{position:absolute;left:96px;width:920px;top:240px;font-size:12.3px;line-height:29px;color:var(--body)}
.seg-body p{margin-bottom:22px}

.folio{position:absolute;right:30px;top:4800px;font-size:13px;color:var(--ink)}
</style>
</head>
<body>

<section class="panel cover">
  <div class="cover-scene" role="img" aria-label="Photograph of a calm alpine lake with snow-capped mountains and a lone tree reflected in still water"></div>
  <div class="brand">
    <span class="brand-mark"></span>
    <div class="brand-name">Bright Path<br>Reading Approach</div>
    <div class="brand-sub">Te Huarahi Pānui</div>
  </div>
</section>

<section class="panel this-week">
  <div class="tw-block" style="top:112px">
    <h2>This week your child’s class is reading</h2>
    <p>Mabel Moth on the Deep Green Sea</p>
    <p>By Hana Rewiti and Lucy Fenn</p>
  </div>
  <div class="tw-block" style="top:267px">
    <h2>Some new words your child is learning</h2>
    <p>Brave means to be ready to face danger and be courageous.</p>
    <p>Depart is when somebody goes away or leaves.</p>
    <p>A breeze is a very light wind.</p>
    <p>Hoist means to lift or haul something up using a mechanical device.</p>
  </div>
  <div class="tw-block" style="top:505px">
    <h2>Some new sounds your child is learning</h2>
    <p>‘m’ as in mud, man and moon</p>
    <p>‘d’ as in duck and dog</p>
  </div>
</section>

<section class="panel play">
  <div class="play-photo" role="img" aria-label="Photograph of a child’s hand pointing at words in an open picture book"></div>
  <div class="play-text">
    <h2>Some fun ways you can play with sounds at home</h2>
    <p>Use playdough, modelling clay, pipe cleaners or even blocks to make the shapes of this week’s letters. Practice making the ‘m’ sound which you’re creating your letters. Talk about how the letter looks, and then brainstorm some words that start with its sound. Your child may remember some of the words from class to start you off! When your child finds a word encourage them to say the name and the letter sound e.g. mug starts with an ‘m’ sound.</p>
    <p>Write the letters and have them around you home – draw your child’s attention to them every time you see them and practice the sound. Hide objects or toys that start with the same letter as the one you are targeting and go on a ‘letter’ treasure hunt – see who can get the most of each letter. When they find them get them to yell out the sound!</p>
    <p>If you are reading a book with them see who can find any words that start with a ‘m’ or a ‘d’ the fastest. If they are able to, get them to read the word aloud, or support them in doing this. Practice making the ‘m’ or ‘d’ sound.</p>
    <p style="margin-top:30px;margin-bottom:4px">To access online versions of the small readers visit</p>
    <p><span class="link">https://www.brightpathreading.nz/for-families</span></p>
  </div>
</section>

<section class="panel lesson">
  <div class="frame week">
    <div class="tab">Week 1</div>
    <div class="week-left">Lesson 1<br>Book: The Night Walk of Tūī and Weka<br>and Kiwi by Mere Tane and Ruby Lawson</div>
    <div class="week-right">
      Target vocabulary: velvety, decorate, marama (moon), rākau (tree)<br>
      Target phoneme/graphemes: m, d<br>
      Target picture card words (English): mop, mat, mad, map, men, dog, dig, dad, dot, den<br>
      Target picture card words (te reo Māori): marama, manu, moe<br>
      Suggested readers: Pat, Tap; Pop, Pop in the Pot; Mot and Don; Dig the Mud
    </div>
  </div>
  <div class="section-head" style="top:320px">
    <h2>Vocabulary Development with Book</h2>
    <p>Objective: Learning about new words, developing listening and oral narrative skills</p>
  </div>
  <div class="frame day" style="top:424px;height:218px">
    <div class="tab">DAY 1</div>
    <div class="day-lead" style="top:20px">Read the story:<br>Use written prompts in the book to introduce and elaborate new vocabulary words.</div>
    <div class="day-body" style="top:102px"><b>Recall the story:</b> Ask children to share something they remember from the story with a friend. Support children with limited oral language skills by using the story book pictures as prompts. E.g., open a page of the story and ask “what can you see on this page?” Use language elicitation and feedback strategies to extend children’s language.</div>
  </div>
</section>

<section class="panel pa">
  <div class="section-head" style="top:64px">
    <h2>Phonological Awareness (PA) Skill Building</h2>
    <p>Objective: Identifying sounds in words (including words from story) and matching phoneme with grapheme.</p>
  </div>
  <div class="frame day" style="top:167px;height:484px">
    <div class="tab">DAY 1</div>
    <div class="day-lead" style="top:18px;right:20px">Phoneme identity:&nbsp; Bring children’s attention to the first sound in words. Write the week’s target sound on the board (or use a large letter card) and run through the picture cards associated with that target sound. Emphasise the target phoneme and grapheme in the word.</div>
    <div class="day-body" style="top:126px">For example: “This week’s story is about two manu or birds who are having adventures at midnight. Midnight is a time in the middle of the night when it is very dark. Dark starts with a /d/ sound (display the large letter card or write on the board). Let’s write the letter together (write in the air or on whiteboards). What sound does it make? /d/! Now let’s find some words that start with a /d/ sound”. Explicitly draw children’s attention to the target sound in the word as you work through the target /d/cards E.g., “Dot starts with /d/ - see the letter d at the beginning of the word, this letter makes the /d/ sound. Listen again for the /d/ at the start of duck.” Work through the target /d/ cards: dog, dig, dad, dot, den.<br><br>GAME<br>Use /d/ words from picture cards as target words, and /m/ words as distractors.<br>Pick out the picture: Place picture cards inside a “special” container (e. g., a kete or bag, or an object related to the story e.g., a ‘honey jar’). Hold the container up so child can’t see the cards inside the container and ask a child to</div>
  </div>
</section>

<section class="panel seg">
  <h2>Segmenting and Blending:</h2>
  <div class="seg-sub">Encourage children to segment and blend words using your chosen game.</div>
  <div class="seg-body">
    <p>GAME Class Segmentation Board: Using a segmentation board on the whiteboard, segment target words and some words from the story. Say the word, and then demonstrate how to segment the word into phonemes by placing a token on a square each time you say a phoneme. Once segmented, blend the phonemes together to read the word. E.g., Target word: “Listen for the sounds in dog: d-o-g, (representing each phoneme with a block or counter) dog - there are three sounds in dog”. After you’ve demonstrated a couple of words, work together as a class to segment words and then blend together again.</p>
    <p>Choose one of the words you have segmented to write on the board using segmentation skills E.g. “I will write the word den - listen for the sounds as I write the word d-e-n. This word says den. A den is somewhere a bear might hide in the winter.” Aim for at least 6 items, segmented and blended and one word to spell on the board using segmentation skills. E.g., d-a-d, d-o-t, d-i-g, d-e-n, d-o-g, m-a-p Sound manipulation: Support children to add, move and manipulate sounds in words using your chosen game.</p>
    <p>GAME On the Board: Using the class whiteboard, complete a manipulation chain activity. Draw 3-4 &nbsp;&nbsp; large squares to use as spaces to write the letter/s (grapheme) that represent each phoneme in the word. Write the grapheme in each square, and start a manipulation chain, changing one letter each time. E.g., Write ‘dot’ on the board in large squares, one letter per square. “This says ‘dot’, let’s make it say ‘hot’. Which letter should I rub out?</p>
  </div>
</section>

<div class="folio">c7</div>

</body>
</html>
```